Informational Site for Advanced Chemistry R&D

The company develops oxidation chemistry for air, water, fuel pollution controls. The site has been prototyped at www.velmirlab.net. Take a look. Now, the task is to design it for eye-catching beauty with use of color, on-page scroll-driven color transition and parallax effects. Should capture the themes: high technology, wow it's beautiful, modern, uncluttered, clean urban environment.

Target Market(s)

China Environmentally Conscious Government and Industry,

Industry/Entity Type

It Company

Number of Pages Required

3 page

Font styles to use
Sans Serif

Requirements
Must have
• Parallax effects, desktop compatible, Rich, Modern, Simple, Graphic
Nice to have
• Mobile Phone Compatible
Should not have
• Flash, or anything that is slow to load or requires high bandwidth

```html
<!DOCTYPE html>
<html lang="en">
<head>
<meta charset="utf-8">
<title>VelmirLab – Advanced Oxidation Science</title>
<link rel="stylesheet" href="https://fonts.googleapis.com/css2?family=Raleway:wght@400;500&family=Carlito:wght@400;700&display=swap">
<style>
  :root {
    --blue: #1a72bb;
    --teal: #2dbcb8;
    --white: #ffffff;
    --paper: #eeeeee;
    --ink: #1c1c1c;
    --grey: #6f6f6f;
    --text-grey: #7c7c7c;
    --photo-dark: #1e1e1e;
  }
  * { margin: 0; padding: 0; box-sizing: border-box; }
  html, body { width: 1008px; height: 1200px; overflow: hidden; }
  body {
    position: relative;
    background: var(--paper);
    font-family: "Carlito", "Lato", sans-serif;
  }

  /* Header / hero */
  .brand {
    position: absolute; left: 0; top: 0; width: 366px; height: 166px;
    background: var(--white);
    display: flex; align-items: center; justify-content: center; gap: 10px;
  }
  .brand-dot { width: 22px; height: 22px; border-radius: 50%; background: var(--teal); }
  .brand-name {
    font-family: "Carlito", sans-serif; font-weight: 700; font-size: 34px;
    color: var(--blue); letter-spacing: 0.5px;
  }

  .intro {
    position: absolute; left: 0; top: 166px; width: 366px; height: 500px;
    background: var(--blue); color: var(--white);
    padding: 38px 30px 0 38px;
  }
  .intro-title {
    font-family: "Raleway", sans-serif; font-weight: 400;
    font-size: 56px; line-height: 60px; letter-spacing: 0.5px;
  }
  .intro-title .spread { letter-spacing: 11.5px; }
  .intro-lead { margin-top: 40px; font-size: 13.6px; line-height: 24px; }
  .intro-caps { margin-top: 22px; font-size: 14.5px; text-transform: uppercase; }
  .intro-body { margin-top: 22px; font-size: 13.6px; line-height: 24px; }

  .hero-photo {
    position: absolute; left: 366px; top: 0; width: 642px; height: 666px;
    background:
      radial-gradient(ellipse at 90% 60%, rgba(120,95,30,0.55), transparent 45%),
      radial-gradient(ellipse at 45% 30%, rgba(90,90,90,0.35), transparent 50%),
      linear-gradient(180deg, #2b2b2b 0%, var(--photo-dark) 60%, #181614 100%);
  }

  .main-nav {
    position: absolute; left: 366px; top: 0; width: 594px; height: 70px;
    border-bottom: 1px solid rgba(255,255,255,0.85);
  }
  .main-nav a {
    position: absolute; top: 36px; color: var(--white);
    text-decoration: none; font-size: 11px; font-family: "Carlito", sans-serif;
  }
  .main-nav a.active { color: var(--teal); }
  .nav-underline {
    position: absolute; left: 11px; bottom: -1px; width: 52px; height: 3px; background: var(--teal);
  }

  /* Services */
  .services-title {
    position: absolute; left: 0; top: 706px; width: 1008px; text-align: center;
    font-family: "Raleway", sans-serif; font-weight: 500; font-size: 29px; color: var(--ink);
  }
  .services-rule {
    position: absolute; left: 433px; top: 746px; width: 105px; height: 2px; background: var(--teal);
  }
  .services-sub {
    position: absolute; left: 0; top: 786px; width: 1008px; text-align: center;
    font-size: 13px; color: var(--grey);
  }
  .connector { position: absolute; left: 188px; top: 879px; width: 622px; height: 1.5px; background: var(--teal); }

  .service {
    position: absolute; top: 821px; width: 240px; text-align: center;
  }
  .service svg { display: block; margin: 0 auto; }
  .service-name {
    margin-top: 17px; font-weight: 700; font-size: 14.5px; letter-spacing: 0.5px; color: var(--blue);
  }
  .service-name.teal { color: var(--teal); }
  .service-text { margin-top: 3px; font-size: 10.5px; line-height: 13.5px; color: var(--text-grey); }
  .read-more {
    display: inline-block; margin-top: 6px; font-size: 10.5px; color: var(--blue); text-decoration: none;
  }
  .read-more.teal { color: var(--teal); }
  .read-more::after {
    content: ""; display: inline-block; margin-left: 6px;
    border-left: 4px solid currentColor; border-top: 3.5px solid transparent; border-bottom: 3.5px solid transparent;
  }

  /* Footer */
  .site-footer {
    position: absolute; left: 0; top: 1118px; width: 1008px; height: 82px; background: var(--teal);
  }
  .copyright {
    position: absolute; left: 0; top: 34px; width: 1008px; text-align: center;
    color: var(--white); font-size: 9px; font-weight: 700;
  }
  .social { position: absolute; left: 818px; top: 36px; display: flex; gap: 20px; }
  .social span { width: 12px; height: 12px; border-radius: 50%; background: rgba(255,255,255,0.35); }
  .social span:first-child { background: var(--white); }
</style>
</head>
<body>

<div class="brand">
  <span class="brand-dot"></span>
  <span class="brand-name">VelmirLab</span>
</div>

<div class="hero-photo" role="img" aria-label="Dimmed photo of workers in hard hats operating drilling equipment over a waste site"></div>

<nav class="main-nav">
  <a class="active" href="#" style="left:22px">Home</a>
  <a href="#" style="left:102px">About Us</a>
  <a href="#" style="left:198px">Technology</a>
  <a href="#" style="left:304px">Products</a>
  <a href="#" style="left:397px">Contact Us</a>
  <span class="nav-underline"></span>
</nav>

<section class="intro">
  <h1 class="intro-title">ADVANCED<br>OXIDATION<br><span class="spread">SCIENCE</span></h1>
  <p class="intro-lead">Lorem ipsum dolor sit amet, consectetur adipiscing elit, sed do tempor incididunt ut labore</p>
  <p class="intro-caps">Lorem ipsum dolor sit amet</p>
  <p class="intro-body">Lorem ipsum dolor sit amet, consectetur adipiscing elit, sed do eiusmod tempor incididunt ut labore et dolore minim veniam magna aliqua.</p>
</section>

<h2 class="services-title">New Ideas For A Cleaner World</h2>
<div class="services-rule"></div>
<p class="services-sub">Environmental pollution control solutions employing nature's most reactive Free Radica</p>
<div class="connector"></div>

<div class="service" style="left:68px">
  <svg width="118" height="118" viewBox="-59 -59 118 118">
    <circle r="57" fill="var(--paper)" stroke="var(--blue)" stroke-width="2.5"/>
    <circle r="52" fill="var(--teal)"/>
    <path d="M0 -36 C8 -18 22 -4 22 10 A22 22 0 0 1 -22 10 C-22 -4 -8 -18 0 -36 Z" fill="var(--white)"/>
  </svg>
  <div class="service-name teal">WATER</div>
  <p class="service-text">Lorem ipsum dolor sit amet, consectetur edit adipiscing elit, sed do eiusmod tempor incididunt utdolore magna aliqua.</p>
  <a class="read-more teal" href="#">Read More</a>
</div>

<div class="service" style="left:378px">
  <svg width="118" height="118" viewBox="-59 -59 118 118">
    <circle r="57" fill="var(--paper)" stroke="var(--teal)" stroke-width="2.5"/>
    <circle r="52" fill="var(--blue)"/>
    <path d="M-22 -18 C-6 -32 26 -24 26 2 C26 22 4 30 -8 20 C-18 11 -12 -6 2 -6 C12 -6 14 6 6 8" fill="none" stroke="var(--white)" stroke-width="8" stroke-linecap="round"/>
  </svg>
  <div class="service-name">AIR</div>
  <p class="service-text">Lorem ipsum dolor sit amet, consectetur edit adipiscing elit, sed do eiusmod tempor incididunt utdolore magna aliqua.</p>
  <a class="read-more" href="#">Read More</a>
</div>

<div class="service" style="left:690px">
  <svg width="118" height="118" viewBox="-59 -59 118 118">
    <circle r="57" fill="var(--paper)" stroke="var(--teal)" stroke-width="2.5"/>
    <circle r="52" fill="var(--blue)"/>
    <rect x="-20" y="-30" width="26" height="52" rx="4" fill="var(--white)"/>
    <rect x="-15" y="-24" width="16" height="10" rx="1.5" fill="var(--blue)"/>
    <rect x="-25" y="22" width="36" height="6" fill="var(--white)"/>
    <path d="M6 -6 H12 V12 A4 4 0 0 0 20 12 V-10 L14 -18" fill="none" stroke="var(--white)" stroke-width="3.5" stroke-linejoin="round"/>
  </svg>
  <div class="service-name">FUEL</div>
  <p class="service-text">Lorem ipsum dolor sit amet, consectetur edit adipiscing elit, sed do eiusmod tempor incididunt utdolore a aliqua.</p>
  <a class="read-more" href="#">Read More</a>
</div>

<footer class="site-footer">
  <p class="copyright">© All Rights Reserved. Copyrights @VelmirLab. 2016</p>
  <div class="social"><span></span><span></span><span></span><span></span><span></span></div>
</footer>

</body>
</html>
```